Tallowreed Advisory Partners Business Card Design

We have the logo we just need someone to design a modern business card design.

Name: Desmond Munkalt
Phone: 3055550148
Mobile: 9175550193
Web:www.tallowreedadvisory.example
email: dmunkalt@tallowreedadvisory.example
Company: Tallowreed Advisory Partners
Title: CEO

Address: 718 Quillmore Ave, Miami, Florida 33190

Target Market(s)

companies over 100 employees

Industry/Entity Type

Business

```html
<!DOCTYPE html>
<html lang="en">
<head>
<meta charset="utf-8">
<title>Tallowreed Advisory Partners – Business Card</title>
<link rel="stylesheet" href="https://fonts.googleapis.com/css2?family=Arimo:wght@400;700&display=swap">
<style>
  :root {
    --backdrop: #2a2a2c;
    --card-dark: #1d1a23;
    --card-dark-shape: #262c4a;
    --brand-blue: #3d63b5;
    --brand-blue-deep: #2f4f9a;
    --paper: #f7f7f8;
    --ink: #1a1a1c;
    --ink-soft: #4a4a50;
  }
  * { box-sizing: border-box; margin: 0; padding: 0; }
  html, body { width: 1200px; height: 900px; overflow: hidden; background: var(--backdrop); }
  body { font-family: "Arimo", Arial, sans-serif; }

  .canvas {
    position: relative; width: 1200px; height: 900px;
    display: flex; flex-direction: column; align-items: center; justify-content: center; gap: 56px;
  }
  .card {
    position: relative; width: 600px; height: 343px; overflow: hidden;
    box-shadow: 0 14px 32px rgba(0,0,0,.45);
  }

  /* Back side */
  .card--back { background: var(--card-dark); }
  .card--back .decor-circle {
    position: absolute; left: 70px; top: -40px; width: 420px; height: 420px;
    border-radius: 50%; background: var(--card-dark-shape);
  }
  .card--back .back-name {
    position: absolute; left: 0; right: 0; top: 138px; text-align: center;
    color: var(--brand-blue); font-weight: 700; font-size: 26px; letter-spacing: .5px;
  }
  .card--back .back-web {
    position: absolute; left: 0; right: 0; top: 250px; text-align: center;
    color: var(--brand-blue); font-size: 15px; letter-spacing: .3px;
  }

  /* Front side */
  .card--front { background: linear-gradient(160deg, #ffffff 0%, var(--paper) 60%, #ececef 100%); }
  .card--front .edge-stripe {
    position: absolute; left: 0; top: 0; bottom: 0; width: 16px; background: var(--brand-blue);
  }
  .brand {
    position: absolute; right: 34px; top: 34px;
    display: flex; flex-direction: column; align-items: flex-end; gap: 10px;
  }
  .brand-dot { width: 44px; height: 44px; border-radius: 50%; background: var(--brand-blue-deep); }
  .brand-name { color: var(--ink); font-weight: 700; font-size: 19px; letter-spacing: .3px; }

  .holder {
    position: absolute; left: 48px; top: 40px;
  }
  .holder-name { color: var(--ink); font-weight: 700; font-size: 20px; letter-spacing: .3px; }
  .holder-title {
    margin-top: 6px; color: var(--brand-blue); font-size: 13px;
    letter-spacing: 2px; text-transform: uppercase;
  }

  .address {
    position: absolute; right: 34px; top: 150px; text-align: right; font-style: normal;
    color: var(--ink-soft); font-size: 15px; line-height: 1.45;
  }

  .contacts {
    position: absolute; left: 48px; bottom: 34px; list-style: none;
    color: var(--ink-soft); font-size: 16px;
  }
  .contacts li { display: flex; align-items: center; gap: 8px; line-height: 1.65; }
  .contact-icon { width: 18px; height: 18px; flex: none; }
</style>
</head>
<body>
<main class="canvas">

  <section class="card card--back" aria-label="Card back">
    <div class="decor-circle"></div>
    <p class="back-name">Tallowreed Advisory Partners</p>
    <p class="back-web">www.tallowreedadvisory.example</p>
  </section>

  <section class="card card--front" aria-label="Card front">
    <div class="edge-stripe"></div>

    <div class="holder">
      <p class="holder-name">Desmond Munkalt</p>
      <p class="holder-title">CEO</p>
    </div>

    <div class="brand">
      <div class="brand-dot"></div>
      <p class="brand-name">Tallowreed Advisory Partners</p>
    </div>

    <address class="address">
      718 Quillmore Ave<br>
      Miami<br>
      Florida 33190
    </address>

    <ul class="contacts">
      <li>
        <svg class="contact-icon" viewBox="0 0 18 18" aria-hidden="true">
          <circle cx="9" cy="9" r="9" fill="#2f4f9a"/>
          <path d="M6 4.5c.6-.3 1 .1 1.3.7l.6 1.3c.2.5 0 .8-.4 1.1-.3.2-.3.5-.1.9.5.9 1.2 1.6 2.1 2.1.4.2.7.2.9-.1.3-.4.6-.6 1.1-.4l1.3.6c.6.3 1 .7.7 1.3-.5 1-1.5 1.5-2.6 1.1-2.3-.8-4.1-2.6-4.9-4.9C5.6 5.1 5.2 4.9 6 4.5z" fill="#fff"/>
        </svg>
        3055 550 148
      </li>
      <li>
        <svg class="contact-icon" viewBox="0 0 18 18" aria-hidden="true">
          <circle cx="9" cy="9" r="9" fill="#2f4f9a"/>
          <rect x="6" y="3.8" width="6" height="10.4" rx="1" fill="#fff"/>
          <rect x="7" y="5" width="4" height="6.8" fill="#2f4f9a"/>
          <circle cx="9" cy="13" r=".6" fill="#2f4f9a"/>
        </svg>
        9175 550 193
      </li>
      <li>
        <svg class="contact-icon" viewBox="0 0 18 18" aria-hidden="true">
          <circle cx="9" cy="9" r="9" fill="#2f4f9a"/>
          <rect x="4.5" y="5.8" width="9" height="6.4" fill="#fff"/>
          <path d="M4.5 5.8 9 9.6l4.5-3.8" fill="none" stroke="#2f4f9a" stroke-width=".9"/>
        </svg>
        dmunkalt@tallowreedadvisory.example
      </li>
    </ul>
  </section>

</main>
</body>
</html>
```